Tallowfen Capital Group - letterhead

We need a corporate letterhead template (word) and slide show template (PowerPoint) designed for our investment business Tallowfen Capital Group.

Tallowfen Capital Group manages a group of investments in Australia and are after a letterhead template and PowerPoint template that is both creative and professional in design.

Information to be included on the letterhead (word) template is as follows:

Level 4, 318 Marlow Road
Kew VIC 3101

t. 03 5127 6618

Please feel free to ask any questions.

Investment

```html
<!DOCTYPE html>
<html lang="en">
<head>
<meta charset="utf-8">
<title>Tallowfen Capital Group – Letterhead</title>
<link href="https://fonts.googleapis.com/css2?family=Lato:wght@400;700&display=swap" rel="stylesheet">
<style>
  :root {
    --brand-blue: #1b5f9e;
    --map-tint: rgba(220, 233, 247, 0.85);
    --map-fade: rgba(220, 233, 247, 0);
    --paper: #ffffff;
    --ink: #1e2a36;
  }
  * { margin: 0; padding: 0; box-sizing: border-box; }
  html, body { width: 849px; height: 1200px; overflow: hidden; background: var(--paper); }
  .letterhead {
    position: relative;
    width: 849px;
    height: 1200px;
    background: var(--paper);
    font-family: "Lato", sans-serif;
    overflow: hidden;
  }
  .side-band {
    position: absolute;
    left: 0; top: 0;
    width: 156px; height: 1200px;
  }
  .brand {
    position: absolute;
    top: 62px;
    left: 156px; right: 0;
    display: flex;
    align-items: center;
    justify-content: center;
    gap: 12px;
    color: var(--brand-blue);
  }
  .brand-mark {
    width: 14px; height: 14px;
    border-radius: 50%;
    background: var(--brand-blue);
  }
  .brand-name {
    font-size: 30px;
    font-weight: 400;
    letter-spacing: 1px;
  }
  .region-visual {
    position: absolute;
    left: 215px; top: 380px;
    width: 560px; height: 520px;
    background: radial-gradient(ellipse 50% 50% at 50% 50%, var(--map-tint) 0%, var(--map-tint) 45%, var(--map-fade) 100%);
  }
  .address-line {
    position: absolute;
    left: 168px;
    top: 1146px;
    font-size: 20px;
    color: var(--ink);
    white-space: nowrap;
  }
</style>
</head>
<body>
  <div class="letterhead">
    <svg class="side-band" viewBox="0 0 156 1200" aria-hidden="true">
      <defs>
        <linearGradient id="bandFill" x1="0" y1="0" x2="0" y2="1">
          <stop offset="0" stop-color="#0d4a85"/>
          <stop offset="0.5" stop-color="#1a5f9f"/>
          <stop offset="1" stop-color="#1d65a8"/>
        </linearGradient>
      </defs>
      <rect width="156" height="1200" fill="url(#bandFill)"/>
      <rect x="148" width="8" height="1200" fill="#3a82c4" opacity="0.55"/>
      <polygon points="0,0 156,0 0,140" fill="#5b97cf" opacity="0.35"/>
      <polygon points="0,1060 156,1200 0,1200" fill="#5b97cf" opacity="0.35"/>
    </svg>

    <header class="brand">
      <span class="brand-mark"></span>
      <span class="brand-name">Tallowfen Capital Group</span>
    </header>

    <div class="region-visual" role="img" aria-label="Light blue map of Australia"></div>

    <footer class="address-line">Address:- Level 4, 318 Marlow Road Kew VIC 3101 t. 03 5127 6618</footer>
  </div>
</body>
</html>
```